Business Card Design Project

I need a business card designed with these details on the front along with the logo attached on the front.

Address - 518/ 217 Wendlebury st Thornvale
Website - www.brackenhollowmasonry.com.au
Email - delwyn@brackenhollowmasonry.com.au
Fax - 1900 457 618
Mobile - 0471926038
Telephone - 1300517926
Licence number - 847263k

```html
<!DOCTYPE html>
<html lang="en">
<head>
<meta charset="utf-8">
<title>Bracken Hollow Masonry – Business Card</title>
<link rel="stylesheet" href="https://fonts.googleapis.com/css2?family=Tinos:wght@400;700&display=swap">
<style>
  :root {
    --page-bg: #f2f2f2;
    --band-orange: #f5931f;
    --rule-brown: #4a2210;
    --text-brown: #4a2414;
    --field-beige: #cdc1a6;
    --tile-cream: #ece3d6;
    --card-shadow: rgba(0, 0, 0, 0.18);
  }
  * { margin: 0; padding: 0; box-sizing: border-box; }
  html, body {
    width: 1200px;
    height: 900px;
    overflow: hidden;
    background: var(--page-bg);
  }
  .canvas {
    position: relative;
    width: 1200px;
    height: 900px;
    display: flex;
    align-items: center;
    justify-content: center;
  }
  .business-card {
    position: relative;
    width: 900px;
    height: 514px;
    background: var(--field-beige);
    box-shadow: 0 12px 30px var(--card-shadow);
    overflow: hidden;
    font-family: "Tinos", "Times New Roman", serif;
    color: var(--text-brown);
  }
  .brand-band {
    position: absolute;
    left: 0; top: 0;
    width: 100%;
    height: 196px;
    background: var(--band-orange);
    border-bottom: 7px solid var(--rule-brown);
  }
  .brand-mark {
    position: absolute;
    left: 292px;
    top: 108px;
    width: 70px;
    height: 70px;
    background: var(--tile-cream);
  }
  .brand-name {
    position: absolute;
    left: 384px;
    top: 64px;
    font-weight: 700;
    font-size: 36px;
    line-height: 40px;
    letter-spacing: 1px;
    text-transform: uppercase;
    color: var(--text-brown);
  }
  .pattern-field {
    position: absolute;
    left: 0; top: 203px;
    width: 100%;
    height: 311px;
    background: var(--field-beige);
  }
  .contact-details {
    position: absolute;
    left: 0; top: 214px;
    width: 100%;
    list-style: none;
    font-size: 24px;
    line-height: 33px;
  }
  .contact-details li { position: relative; white-space: nowrap; }
  .contact-details .line-address { padding-left: 296px; }
  .contact-details .line-website { padding-left: 316px; }
  .contact-details .line-email   { padding-left: 318px; }
  .contact-details .line-fax     { padding-left: 462px; }
  .contact-details .line-mobile,
  .contact-details .line-phone,
  .contact-details .line-licence { padding-left: 452px; }
</style>
</head>
<body>
<main class="canvas">
  <article class="business-card">
    <header class="brand-band">
      <div class="brand-mark"></div>
      <h1 class="brand-name">Bracken Hollow<br>Masonry</h1>
    </header>
    <div class="pattern-field" role="img" aria-label="Beige background with a repeating pattern of soft cream rounded stone tiles"></div>
    <ul class="contact-details">
      <li class="line-address">Address - 518/ 217 Wendlebury st Thornvale</li>
      <li class="line-website">Website - www.brackenhollowmasonry.com.au</li>
      <li class="line-email">Email - delwyn@brackenhollowmasonry.com.au</li>
      <li class="line-fax">Fax - 1900 457 618</li>
      <li class="line-mobile">Mobile - 0471926038</li>
      <li class="line-phone">Telephone - 1300517926</li>
      <li class="line-licence">Licence number - 847263k</li>
    </ul>
  </article>
</main>
</body>
</html>
```